Serene Mind-Rest: Quiet Hour Now, Inc.
Create business card, stationery, envelope design
Professional
Marisol T. Okafor, RN, MSN
Founder/Director
712 Harrowgate Lane, Suite PK3
Brooklyn, New York 11347
Marisol@Quiethournow.com
www.Quiethournow.com
Please use the following pantone colors:
purple [266], blue [279] and yellow [123]
Use purple [266] for font on back of card
Enlightening Others Is Empowerment
Empowering Others Is ~ Serene Mind-Rest: Quiet Hour Now
Serene Mind-Rest: Quiet Hour Now ~ Is Loving Myself®™
Hello Designers,
I uploaded my current business card so that you can see what I have already.
I just realized after comparing both cards, I did not add my roles on the business card project!
Please add:
Self-Care Specialist
Holistic Nurse Educator
Certified Wellness Coach/Speaker
Thank you,
Marisol

```html
<!DOCTYPE html>
<html lang="en">
<head>
<meta charset="utf-8">
<title>Serene Mind-Rest: Quiet Hour Now, Inc. — Stationery</title>
<link href="https://fonts.googleapis.com/css2?family=Open+Sans:wght@400;600;700&display=swap" rel="stylesheet">
<style>
:root{
  --purple:#6b3fa8;
  --purple-soft:#b9a3d8;
  --blue:#418fde;
  --yellow:#ffc72c;
  --paper:#ffffff;
  --ground:#e6e3df;
  --ink:#5a4a78;
}
*{margin:0;padding:0;box-sizing:border-box}
html,body{width:1200px;height:667px;overflow:hidden}
body{background:var(--ground);font-family:"Open Sans",Arial,sans-serif;color:var(--ink);position:relative}
.sheet{position:absolute;background:var(--paper);box-shadow:0 2px 6px rgba(0,0,0,.18);overflow:hidden}
.edge{position:absolute;top:0;bottom:0;display:flex;flex-direction:column}
.edge .y{background:var(--yellow);height:14px}
.edge .b{background:var(--blue);height:14px}
.edge .p{background:var(--purple);flex:1}
.brand{display:flex;align-items:center;gap:6px;position:absolute}
.brand .dot{width:14px;height:14px;border-radius:50%;background:var(--yellow);flex:none}
.brand .name{font-weight:700;color:var(--purple);line-height:1.1}
.tag{position:absolute;font-size:6px;color:var(--purple)}
.small{font-size:6px;line-height:1.5;color:var(--ink)}

/* envelope front */
.env-front{left:53px;top:24px;width:386px;height:214px}
.env-front .edge{left:0;width:18px}
.env-front .brand{left:40px;top:18px}
.env-front .brand .name{font-size:10px}
.env-front .tag{left:60px;top:46px}
.env-front .return{position:absolute;left:30px;bottom:14px}

/* envelope back */
.env-back{left:53px;top:247px;width:386px;height:245px}
.env-back svg{position:absolute;left:0;top:0}
.env-back .mark{position:absolute;left:175px;top:46px;width:36px;height:36px;border-radius:50%;background:var(--purple-soft);opacity:.55}

/* letterhead */
.letterhead{left:470px;top:24px;width:399px;height:526px}
.letterhead .edge{left:0;width:14px}
.letterhead .brand{left:34px;top:22px}
.letterhead .brand .name{font-size:11px}
.letterhead .tag{left:56px;top:52px}
.letterhead .sender{position:absolute;right:26px;top:24px;font-size:6px;line-height:1.5}
.letterhead .sender strong{font-weight:600;color:var(--purple)}
.letterhead .footer{position:absolute;left:34px;right:20px;bottom:14px;font-size:5px;color:var(--ink);white-space:nowrap}

/* card front */
.card-front{left:883px;top:24px;width:283px;height:178px}
.card-front .edge{right:0;width:10px}
.card-front .who{position:absolute;left:14px;top:10px;font-size:6px;line-height:1.5}
.card-front .who strong{font-weight:600;color:var(--purple);font-size:7px}
.card-front .brand{left:14px;top:90px}
.card-front .brand .name{font-size:10px}
.card-front .tag{left:34px;top:118px}
.card-front .where{position:absolute;right:22px;top:84px;font-size:6px;line-height:1.5;text-align:right}

/* card back */
.card-back{left:883px;top:230px;width:283px;height:173px}
.card-back .edge{left:0;width:10px}
.card-back .brand{left:22px;top:14px}
.card-back .brand .name{font-size:9px}
.card-back .lines{position:absolute;left:22px;top:66px;font-size:6.5px;line-height:1.6;color:var(--purple)}
.card-back .web{position:absolute;left:22px;top:124px;font-size:7px;color:var(--purple);font-weight:600}
</style>
</head>
<body>

<section class="sheet env-front" aria-label="Envelope front">
  <div class="edge"><span class="y"></span><span class="b"></span><span class="p"></span></div>
  <div class="brand"><span class="dot"></span><span class="name">Serene Mind-Rest:<br>Quiet Hour Now, Inc.</span></div>
  <p class="tag">Empowering Others Through Daily Wellness</p>
  <p class="return small">712 Harrowgate Lane, Suite PK3<br>Brooklyn, New York 11347</p>
</section>

<section class="sheet env-back" aria-label="Envelope back">
  <svg width="386" height="245" viewBox="0 0 386 245" aria-hidden="true">
    <polygon points="0,0 386,0 386,40 193,92 0,40" fill="var(--purple)"/>
  </svg>
  <div class="mark"></div>
</section>

<section class="sheet letterhead" aria-label="Letterhead">
  <div class="edge"><span class="y"></span><span class="b"></span><span class="p"></span></div>
  <div class="brand"><span class="dot"></span><span class="name">Serene Mind-Rest:<br>Quiet Hour Now, Inc.</span></div>
  <p class="tag">Empowering Others Through Daily Wellness</p>
  <p class="sender"><strong>Marisol T. Okafor, RN, MSN</strong><br>Founder/Director</p>
  <p class="footer">712 Harrowgate Lane, Suite PK3, Brooklyn, New York 11347 &nbsp;|&nbsp; Phone: (718) 555-0142 &nbsp;|&nbsp; Marisol@Quiethournow.com &nbsp;|&nbsp; www.Quiethournow.com</p>
</section>

<section class="sheet card-front" aria-label="Business card front">
  <div class="edge"><span class="p"></span><span class="b"></span><span class="y"></span></div>
  <p class="who"><strong>Marisol T. Okafor, RN, MSN</strong><br>Founder/Director<br>Self-Care Specialist<br>Holistic Nurse Educator<br>Certified Wellness Coach/Speaker</p>
  <div class="brand"><span class="dot"></span><span class="name">Serene Mind-Rest:<br>Quiet Hour Now</span></div>
  <p class="tag">Empowering Others Through Daily Wellness</p>
  <p class="where">712 Harrowgate Lane, Suite PK3<br>Brooklyn, New York 11347<br>Phone: (718) 555-0142<br>Marisol@Quiethournow.com</p>
</section>

<section class="sheet card-back" aria-label="Business card back">
  <div class="edge"><span class="y"></span><span class="b"></span><span class="p"></span></div>
  <div class="brand"><span class="dot"></span><span class="name">Serene Mind-Rest:<br>Quiet Hour Now</span></div>
  <p class="lines">Enlightening Others Is Empowerment<br>Calm Begins With One Quiet Hour<br>Rest Well, Live Well, Care Well</p>
  <p class="web">www.Quiethournow.com</p>
</section>

</body>
</html>
```